Lark Vale Perks Needs a Website Design

We need a website design for a new service we are starting. Users enter a coupon in a redemption page and either create an account or sign in. they can then use the credits they accumulate from the coupons to purchase items listed on the site.

we need a design for the following:
-the coupon redemption page (with a choice to either sign in or create an account)
-a product listing page (with search filters and a search bar. the search bar can be displayed in the header of the site)
-a product detail page, showing the product's title, image, credit redemption value, brand and any category associated with the item
-a my account page, with:
*a list of the pluses (coupons/credit added to account) and the minuses (orders placed/credits subtracted from account) to show a detailed description of their history on the site)
*an area for users to edit their name, phone number, address etc
*an area for users to add / edit their casino membership number and casino
*an area for users to add a coupon to their account
-a cart / checkout process:
*cart displaying items and their total
*entering / selecting an address from their account
*review order details page where they can submit their order (and warning the user that doing so will subtract the required credits from their account)

remember that no ecommerce or money is used on the site.. users are spending their credits and checkout their cart with the credits they accumulated, so the items each have a credit redemption value and the checkout process is shown in credits.

we are not very particular with any design preference, other than we'd like it to be predominately white.

If designing the site with css please make sure to use bootstrap in your designs. thanks!

Target Market(s)

adults 45-65

Industry/Entity Type

Casino

Coding

Coded - Design and coding required

Number of Pages Required

5+ page

Font styles to use
Sans Serif

Requirements
Must have
• css must use with bootstrap
Nice to have
• simplified, easy interface. we are targeting an older crowd and dont want to confuse them
Should not have
• the site shouldnt have any dollar values. all product prices, checkout totals and user accrual's (in the my account page) should be in credits

```html
<!DOCTYPE html>
<html lang="en">
<head>
<meta charset="utf-8">
<title>Lark Vale Perks – Redeem</title>
<link rel="stylesheet" href="https://fonts.googleapis.com/css2?family=Open+Sans:wght@400;600;700&display=swap">
<style>
:root{
  --ink:#2b3640;
  --muted:#7b8690;
  --dark:#1f2a33;
  --navy:#22313f;
  --teal:#2fae91;
  --teal-deep:#23957b;
  --hero-a:#3aa89c;
  --hero-b:#79cbc0;
  --blue:#2a8fd6;
  --line:#dfe4e8;
  --soft:#f2f4f5;
  --white:#ffffff;
}
*{box-sizing:border-box;margin:0;padding:0}
html,body{width:702px;height:1200px;overflow:hidden}
body{font-family:"Open Sans",Arial,sans-serif;color:var(--ink);background:var(--white);font-size:11px;position:relative}
a{color:inherit;text-decoration:none}

.topbar{height:18px;background:var(--dark);color:#cfd6dc;font-size:8px;display:flex;align-items:center;justify-content:space-between;padding:0 24px;text-transform:uppercase;letter-spacing:.3px}
.topbar nav{display:flex;gap:18px}
.topbar .create{text-transform:none}

.header{height:64px;display:flex;align-items:center;padding:0 28px;justify-content:space-between}
.brand-name{font-size:19px;font-weight:700;color:var(--navy);line-height:1}
.brand-tag{font-size:10px;color:var(--muted);margin-top:3px}
.header-tools{display:flex;align-items:center;gap:22px}
.btn-coupon{background:var(--teal);color:#fff;font-size:9px;font-weight:700;padding:7px 16px;border-radius:2px}
.balance{font-size:7px;color:var(--muted);line-height:1.4}
.balance strong{display:block;color:var(--ink);font-size:10px}
.cart{display:flex;align-items:center;gap:6px;font-size:7px;color:var(--muted);line-height:1.3}
.cart strong{display:block;color:var(--ink);font-size:9px}

.mainnav{height:24px;border-top:1px solid var(--line);border-bottom:1px solid var(--line);display:flex;align-items:center;justify-content:space-between;padding:0 28px}
.mainnav ul{display:flex;list-style:none;gap:26px;font-size:8px}
.mainnav li:first-child{font-weight:700}
.search{display:flex;gap:4px;align-items:center}
.search span{height:16px;border:1px solid var(--line);font-size:7px;color:#a4adb4;padding:3px 6px}
.search .q{width:94px}
.search .cat{width:74px}
.search .go{background:var(--navy);color:#fff;font-size:8px;font-weight:700;padding:3px 12px;border:0}

.hero{position:absolute;top:120px;left:0;width:702px;height:310px;background:linear-gradient(135deg,var(--hero-a),var(--hero-b) 55%,var(--hero-a));overflow:hidden}
.hero-product{position:absolute;right:-10px;top:8px;width:250px;height:240px;border-radius:40px;background:radial-gradient(circle at 45% 45%,#eef1f3,#8f979d 55%,#2a2f33 80%)}
.coupon-field{position:absolute;left:70px;top:22px;width:560px;height:28px;background:rgba(255,255,255,.92);font-size:9px;color:#9aa4ab;padding:8px 12px;text-transform:uppercase}
.forms{position:absolute;left:70px;top:80px;width:560px;height:200px;background:rgba(255,255,255,.28);display:flex;gap:16px;padding:16px 14px}
.forms h2{font-size:10px;color:#fff;font-weight:700;margin-bottom:10px;letter-spacing:.3px}
.register{flex:1.1}
.signin{flex:1}
.field-grid{display:grid;grid-template-columns:1fr 1fr;gap:7px 8px}
.field{height:20px;background:#fff;font-size:7px;color:#a9b1b7;padding:5px 7px}
.field.half{width:50%}
.btn-blue,.btn-teal{display:block;margin:12px auto 0;color:#fff;font-size:8px;font-weight:700;text-align:center;padding:6px 0;text-transform:uppercase}
.btn-blue{background:var(--blue);width:60%}
.btn-teal{background:var(--teal-deep);width:100%}
.signin .field{margin-bottom:7px}
.arrow{position:absolute;top:134px;width:14px;height:28px;background:rgba(255,255,255,.85);display:flex;align-items:center;justify-content:center}
.arrow.left{left:0}.arrow.right{right:0}

.how{position:absolute;top:430px;left:0;width:702px;height:180px;text-align:center}
.how h2{font-size:12px;font-weight:700;margin-top:40px;letter-spacing:.4px}
.steps{display:flex;justify-content:center;align-items:flex-start;gap:14px;margin-top:20px}
.step{width:160px}
.step-box{height:40px;border:1px solid var(--line);display:flex;align-items:center;gap:8px;padding:0 10px;text-align:left;font-size:9px;font-style:italic;font-weight:600;line-height:1.15}
.step p{font-size:7px;color:#9aa3aa;margin-top:8px;line-height:1.45;padding:0 10px}
.step-arrow{margin-top:14px}

.promo{position:absolute;top:610px;left:0;width:702px;height:164px;display:flex}
.promo-text{width:351px;background:var(--teal);color:#fff;padding:26px 44px;text-align:center}
.promo-text h3{font-size:11px;font-weight:700;margin-bottom:10px}
.promo-text p{font-size:7.5px;line-height:1.5;text-align:left}
.btn-outline{display:inline-block;margin-top:12px;border:1px solid #fff;font-size:7px;padding:4px 12px;text-transform:uppercase}
.promo-photo{width:351px;background:linear-gradient(160deg,#6b4a3a,#3b5a4c 55%,#2f6b58);position:relative;display:flex;align-items:center;justify-content:flex-end;padding-right:34px}
.promo-title{color:#fff;text-align:center;font-weight:600;letter-spacing:2px;line-height:1.05}
.promo-title small{display:block;font-size:13px}
.promo-title span{display:block;font-size:24px;font-weight:700}

.footer{position:absolute;top:774px;left:0;width:702px;height:406px;background:var(--soft);display:flex;padding:38px 30px 0;gap:20px}
.footer-col{flex:1}
.footer h4{font-size:11px;font-weight:600;margin-bottom:14px}
.footer ul{list-style:none;font-size:9.5px;color:#56626c;line-height:1.8}
.contact p{font-size:9.5px;color:#56626c;line-height:1.6;margin-bottom:10px}
.social{display:flex;gap:6px;margin-top:4px}
.social span{width:20px;height:20px;display:block}
.copyright{position:absolute;bottom:0;left:0;width:702px;height:20px;background:var(--dark);color:#aeb7bf;font-size:7px;padding:6px 24px}
</style>
</head>
<body>

<div class="topbar">
  <nav><a>Login</a><a class="create">Create Account</a></nav>
  <nav><a>My Account</a><a>Checkout</a></nav>
</div>

<header class="header">
  <div class="brand">
    <div class="brand-name">Lark Vale Perks</div>
    <div class="brand-tag">Slogan here</div>
  </div>
  <div class="header-tools">
    <a class="btn-coupon">ADD COUPON</a>
    <div class="balance">Credit balance<strong>4444 cr</strong></div>
    <div class="cart">
      <svg width="18" height="16" viewBox="0 0 18 16" fill="none" stroke="#2b3640" stroke-width="1.5"><path d="M1 1h3l2 9h9l2-6H5"/><circle cx="7" cy="14" r="1.3"/><circle cx="14" cy="14" r="1.3"/></svg>
      <div>my cart<strong>(0) items</strong></div>
    </div>
  </div>
</header>

<div class="mainnav">
  <ul><li>HOME</li><li>Help</li><li>Products</li><li>Contact Us</li></ul>
  <div class="search"><span class="q">Search items</span><span class="cat">Search filters</span><span class="go">SEARCH</span></div>
</div>

<section class="hero">
  <div class="hero-product" role="img" aria-label="Smart watch product shown at an angle"></div>
  <div class="coupon-field">Coupon code</div>
  <div class="forms">
    <div class="register">
      <h2>CREATE AN ACCOUNT</h2>
      <div class="field-grid">
        <div class="field">First name</div><div class="field">Last name</div>
        <div class="field">Email</div><div class="field">Phone</div>
        <div class="field">Password</div><div class="field">Confirm</div>
      </div>
      <div class="field half" style="margin-top:7px">Casino no.</div>
      <a class="btn-blue">Create an account</a>
    </div>
    <div class="signin">
      <h2>SIGN-IN</h2>
      <div class="field">Email address</div>
      <div class="field">Password</div>
      <a class="btn-teal">Sign in</a>
    </div>
  </div>
  <span class="arrow left"><svg width="6" height="10"><path d="M5 1L1 5l4 4" stroke="#2b3640" fill="none" stroke-width="1.5"/></svg></span>
  <span class="arrow right"><svg width="6" height="10"><path d="M1 1l4 4-4 4" stroke="#2b3640" fill="none" stroke-width="1.5"/></svg></span>
</section>

<section class="how">
  <h2>HOW IT WORKS</h2>
  <div class="steps">
    <div class="step">
      <div class="step-box"><svg width="18" height="16" viewBox="0 0 18 16"><rect x="1" y="6" width="16" height="9" fill="#2b3640"/><rect x="0" y="3" width="18" height="4" fill="#2b3640"/><rect x="8" y="3" width="2" height="12" fill="#fff"/></svg>get gift giveaway from casino</div>
      <p>Collect a gift card at your casino and keep the code printed on the back.</p>
    </div>
    <svg class="step-arrow" width="14" height="12"><path d="M0 6h12M7 1l5 5-5 5" stroke="#9aa3aa" fill="none" stroke-width="1.4"/></svg>
    <div class="step">
      <div class="step-box"><svg width="20" height="14" viewBox="0 0 20 14"><rect x="1" y="1" width="18" height="12" rx="1" fill="none" stroke="#2b3640" stroke-width="1.5"/><path d="M4 5h12M4 9h8" stroke="#2b3640" stroke-width="1.5"/></svg>redeem code online</div>
      <p>Enter the code on this page to add the credits to your account balance.</p>
    </div>
    <svg class="step-arrow" width="14" height="12"><path d="M0 6h12M7 1l5 5-5 5" stroke="#9aa3aa" fill="none" stroke-width="1.4"/></svg>
    <div class="step">
      <div class="step-box"><svg width="18" height="16" viewBox="0 0 18 16" fill="none" stroke="#2b3640" stroke-width="1.5"><path d="M1 1h3l2 9h9l2-6H5"/><circle cx="7" cy="14" r="1.3"/><circle cx="14" cy="14" r="1.3"/></svg>shop for products</div>
      <p>Browse the shop and spend your credits on items delivered to your door.</p>
    </div>
  </div>
</section>

<section class="promo">
  <div class="promo-text">
    <h3>Lorem Ipsum is a dummy text</h3>
    <p>Lorem Ipsum is simply dummy text of the printing and typesetting industry. Lorem Ipsum has been the industry's standard dummy text ever since the 1500s, when an unknown printer took a galley of type and scrambled it to make a type specimen book.</p>
    <a class="btn-outline">Learn more</a>
  </div>
  <div class="promo-photo" role="img" aria-label="Casino guests gathered around a roulette table">
    <div class="promo-title"><small>HOW TO USE</small><span>COUPONS</span></div>
  </div>
</section>

<footer class="footer">
  <div class="footer-col">
    <h4>Learn More</h4>
    <ul><li>Tell me about the programme</li><li>What can I earn points on?</li><li>How do I become a member?</li><li>How do I use coupons</li><li>I have some questions</li></ul>
  </div>
  <div class="footer-col">
    <h4>About Points</h4>
    <ul><li>How do I earn points?</li><li>Browse the Rewards Shop</li><li>What are Dream Rewards?</li><li>How to Purchase Products</li><li>My Account</li></ul>
  </div>
  <div class="footer-col contact">
    <h4>Contact Us</h4>
    <p>Phone: 0700 555 014</p>
    <p>Harbour Office 14 Fernleigh Rd,<br>Eastbrook, QLD</p>
    <div class="social">
      <span style="background:#3b5998"></span>
      <span style="background:#1da1f2"></span>
      <span style="background:#d63b2a"></span>
      <span style="background:#e07a2c"></span>
    </div>
  </div>
</footer>

<div class="copyright">Copyright 2016, Lark Vale Perks. All Rights Reserved</div>

</body>
</html>
```